Medical Prescription for Diagnostic Sleep Testing

Quiet Harbor Rest Labs main marketing tool is our Prescription that we leave with medical providers. Prescription is printed on 8.5 x 11 sheets of paper to create a prescription pad for our medical providers. Prescription should fit to one page. Quiet Harbor Rest Labs works with 250 different medical providers so it is important we are able to update and change the medical provider information at bottom. The medical provider would fill-out top with patient information, check-off center testing and patient co-morbidity and Fax to Quiet Harbor Rest Labs. Because it is Faxed to us it is important to have clear print and large font Attached or uploaded file is one example we currently use. Please review all 5 must haves.

Target Market(s)

Prescription for medical providers to fill-out and fax to Quiet Harbor Rest Labs to conduct the sleep study.

Industry/Entity Type

Medical

Colors

Designer to choose only greyscale colors for use in the design.

Requirements
Must have
• 1) Prescription Size: 8.5 x 11
• 2) Must fit to One page Only
• 3) Ability to change medical provider information at bottom of prescription. We work with 250 different medical providers
• 4) Ability to change or update any part of prescription
• 5) Document Must be created in Microsoft Word 2016. This is the program we use for our prescriptions.
Nice to have
• Can be done in Gray-Scale or Black and White since its being faxed from the medical provider to us.

```html
<!DOCTYPE html>
<html lang="en">
<head>
<meta charset="utf-8">
<title>Sleep Study Physician Order</title>
<link rel="stylesheet" href="https://fonts.googleapis.com/css2?family=Montserrat:wght@400;600;700;800&family=Lato:wght@400;700&display=swap">
<style>
:root{
  --ink:#1d1d1d;
  --paper:#ffffff;
  --band:#e4e4e4;
  --rule:#6a6a6a;
  --stage:#ededed;
  --muted:#444444;
}
*{box-sizing:border-box;margin:0;padding:0}
html,body{width:1200px;height:750px;overflow:hidden;background:var(--stage)}
body{font-family:"Lato",sans-serif;color:var(--ink)}
.order-sheet{position:absolute;left:322px;top:15px;width:556px;height:720px;background:var(--paper);display:flex;flex-direction:column;box-shadow:0 2px 8px rgba(0,0,0,.15)}
.sheet-header{display:flex;height:62px}
.brand{width:150px;display:flex;align-items:center;gap:6px;padding-left:14px}
.brand-mark{width:12px;height:12px;border:1.5px solid var(--ink)}
.brand-name{font-family:"Montserrat",sans-serif;font-weight:700;font-size:10px;line-height:1.1;width:90px}
.title-band{flex:1;background:var(--ink);color:var(--paper);display:flex;flex-direction:column;justify-content:center;padding-left:22px;clip-path:polygon(14px 0,100% 0,100% 100%,0 100%)}
.title-band h1{font-family:"Montserrat",sans-serif;font-weight:800;font-size:20px;letter-spacing:.5px}
.title-band p{font-family:"Montserrat",sans-serif;font-size:6.5px;margin-top:4px}
.patient-fields{display:grid;grid-template-columns:1fr 1fr;column-gap:26px;row-gap:9px;padding:12px 22px 10px}
.field{display:flex;align-items:flex-end;gap:5px;font-family:"Montserrat",sans-serif;font-size:9px}
.field span{white-space:nowrap}
.field i{flex:1;border-bottom:1px solid var(--rule);height:9px}
.section-pill{align-self:center;background:var(--ink);color:var(--paper);font-family:"Montserrat",sans-serif;font-weight:700;font-size:11.5px;padding:3px 18px;border-radius:12px;position:relative;z-index:1}
.study-orders{background:var(--band);margin-top:-10px;padding:16px 22px 10px;display:flex;flex-direction:column;gap:5px}
.order-item{display:flex;gap:9px;align-items:flex-start;font-size:7.4px;line-height:1.25}
.checkbox{flex:none;width:11px;height:11px;border:1.2px solid var(--ink);background:var(--paper);margin-top:1px}
.necessity{margin:10px 22px 0;display:flex;flex-direction:column}
.necessity-box{border:1px solid var(--ink);margin-top:-9px;padding:14px 10px 8px;display:grid;grid-template-columns:1fr 1fr 1fr;gap:8px}
.necessity-box ul{list-style:none;display:flex;flex-direction:column;gap:3px}
.necessity-box li{font-size:7.8px;display:flex;align-items:center;gap:6px}
.necessity-box li::before{content:"";width:5px;height:5px;border:1px solid var(--ink);border-radius:50%;flex:none}
.necessity-box .blank{display:inline-block;width:60px;border-bottom:1px solid var(--rule);height:8px}
.provider{flex:1;display:flex;flex-direction:column;padding:12px 22px 0}
.provider-contact{display:flex;justify-content:space-between;font-family:"Montserrat",sans-serif;font-size:8.5px;margin-top:6px;color:var(--muted)}
.provider-list{display:grid;grid-template-columns:repeat(3,1fr);gap:9px 12px;margin-top:10px}
.provider-entry{display:flex;gap:6px;align-items:flex-start}
.provider-entry b{display:block;font-family:"Montserrat",sans-serif;font-size:8.5px}
.provider-entry small{display:block;font-size:7.5px;color:var(--muted)}
.sign-row{display:flex;gap:24px;margin-top:auto;padding-bottom:12px;font-family:"Montserrat",sans-serif;font-size:9px}
.sign-row .field:first-child{flex:2}
.sign-row .field:last-child{flex:1}
.sheet-footer{background:var(--ink);color:var(--paper);text-align:center;font-family:"Montserrat",sans-serif;font-size:8.5px;font-weight:600;padding:6px 0}
</style>
</head>
<body>
<main class="order-sheet">
  <header class="sheet-header">
    <div class="brand"><span class="brand-mark"></span><span class="brand-name">Quiet Harbor Rest Labs</span></div>
    <div class="title-band">
      <h1>SLEEP STUDY PHYSICIAN ORDER</h1>
      <p>Phone: (555) 210-4470 • Fax: (555) 210-4471 • 480 Lanternwood Avenue, Suite 12, Brookvale, NV 89000</p>
    </div>
  </header>

  <section class="patient-fields">
    <div class="field"><span>Patient Name</span><i></i></div>
    <div class="field"><span>DOB</span><i></i></div>
    <div class="field"><span>Telephone</span><i></i></div>
    <div class="field"><span>Alternate Telephone</span><i></i></div>
    <div class="field"><span>Primary Insurance</span><i></i></div>
    <div class="field"><span>Secondary Insurance</span><i></i></div>
    <div class="field"><span>Height</span><i></i><span>Weight</span><i></i></div>
    <div class="field"><span>Patient Gender (circle one)&nbsp; M / F</span></div>
  </section>

  <div class="section-pill">Diagnostic Sleep Study Ordered</div>
  <section class="study-orders">
    <div class="order-item"><span class="checkbox"></span><p>COMPLETE SLEEP STUDY - (Based on Insurance or Patient's Choice) ... In-Lab Sleep Study (PSG) or Home Sleep Study (PSG 95810 / HST 95806) with follow-up PAP Titration Study (PAP 95811 if positive for sleep apnea)</p></div>
    <div class="order-item"><span class="checkbox"></span><p>PEDIATRIC SLEEP STUDY: PSG w/ End Tidal CO2 Monitoring (PSG 95782 under 6 years of age &amp; PSG 95810 older than 6 years of age)</p></div>
    <div class="order-item"><span class="checkbox"></span><p>In-Lab Diagnostic Sleep Study/Polysomnogram (PSG 95810)</p></div>
    <div class="order-item"><span class="checkbox"></span><p>SPLIT-NIGHT STUDY (PSG with PAP 95810 &amp; 95811) To Comply With Accreditation &amp; Insurance Guidelines: ______ AHI must be 20 or greater with minimum 2 hours recorded sleep time and 3 hours minimum to complete PAP treatment.</p></div>
    <div class="order-item"><span class="checkbox"></span><p>CPAP/BiPAP/BiPAP ST Titration Study (Patients with documented sleep apnea 95811)</p></div>
    <div class="order-item"><span class="checkbox"></span><p>Home Sleep Study (HST 95806 Conducted in patient's home &amp; unattended by technologist) (No insurance patient cost $250.00)</p></div>
  </section>

  <section class="necessity">
    <div class="section-pill">Patient Medical Necessity – Please Check All Boxes That Apply</div>
    <div class="necessity-box">
      <ul>
        <li>Atrial Fibrillation</li><li>Bipolar Disorder</li><li>Congestive Heart Failure</li><li>COPD</li><li>Depression</li><li>Excessive Daytime Sleepiness</li><li>Gasping Sensations with Sleep</li><li>Frequent Awakenings</li><li>Frequent Urination</li>
      </ul>
      <ul>
        <li>Heart Disease</li><li>History Heart Attack</li><li>Hypertension</li><li>Insomnia</li><li>Mental or Mood Disorder</li><li>Loud Snoring</li><li>Morbid Obesity / Obesity</li><li>Morning Headaches</li><li>Narcolepsy</li>
      </ul>
      <ul>
        <li>Opioid Use</li><li>PTSD</li><li>Pulmonary Disease</li><li>Restless Leg Syndrome</li><li>Seizures</li><li>Shift Work Sleep disorder</li><li>Stroke / TIA</li><li>Witnessed Apnea</li><li>Other <span class="blank"></span></li>
      </ul>
    </div>
  </section>

  <section class="provider">
    <div class="section-pill">Silverline Ear + Sinus Clinic</div>
    <div class="provider-contact">
      <span>2175 Meadowgate Drive, Brookvale, NV 89000-0142</span>
      <span>Telephone: 555-318-6620</span>
      <span>Fax: 555-318-6621</span>
    </div>
    <div class="provider-list">
      <div class="provider-entry"><span class="checkbox"></span><div><b>Dr. Martin Ellery Voss</b><small>NPI: 1000000101</small></div></div>
      <div class="provider-entry"><span class="checkbox"></span><div><b>Dr. Owen R. Calder</b><small>NPI: 1000000303</small></div></div>
      <div class="provider-entry"><span class="checkbox"></span><div><b>Dr Philip A. Brennick</b><small>NPI: 1000000505</small></div></div>
      <div class="provider-entry"><span class="checkbox"></span><div><b>Dr. Helena Marsh</b><small>NPI: 1000000202</small></div></div>
      <div class="provider-entry"><span class="checkbox"></span><div><b>Lena Thornbury, FNP-C</b><small>NPI: 1000000404</small></div></div>
      <div class="provider-entry"><span class="checkbox"></span><div><b>Noah Pratley, PA-C</b><small>NPI: 1000000606</small></div></div>
    </div>
    <div class="sign-row">
      <div class="field"><span>Physician's Signature:</span><i></i></div>
      <div class="field"><span>Date:</span><i></i></div>
    </div>
  </section>

  <footer class="sheet-footer">Please Fax: 555-210-4471 or Email: orders@quietharborrest.example</footer>
</main>
</body>
</html>
```